New Architectural Firm Business Cards

New Business card to compliment previous pixel forum logo (attached). Please design a business card that is simple, modern, creative....please do not use "symbols", simply the logo and associated graphics/text. The front should contain name/address/phone/email/web address (with graphics).....back should be 100% graphic design using the logo somehow. Hoping for a two color (black and yellow) design. full bleed design, no borders

Target Market(s)

Commercial Architecture Clients

Industry/Entity Type

Architecture

Contact Information for Business Card

Please design a business card that is simple, modern, creative....please do not use "symbols", simply the logo and associated graphics/text. The front should contain name/address/phone/email/web address (with graphics).....back should be 100% graphic design using the logo somehow

Font styles to use
Sans Serif

Colors
FFF300
FFF600
FEFA6F
FFFEC7
FFFEE8

Requirements
Must have
• Clean, Modern Design
Should not have
• Stock images or "icons"

```html
<!DOCTYPE html>
<html lang="en">
<head>
<meta charset="utf-8">
<title>Pixel Forum – Business Cards</title>
<link rel="stylesheet" href="https://fonts.googleapis.com/css2?family=Montserrat:wght@400;500;600;700;800&display=swap">
<style>
  :root {
    --backdrop: #262626;
    --card-white: #ffffff;
    --card-dark: #2f2f2f;
    --brand-yellow: #f6c400;
    --ink: #1c1c1c;
    --ink-soft: #555555;
    --pattern-light: #6a6a6a;
    --pattern-dark: #353535;
  }
  * { box-sizing: border-box; margin: 0; padding: 0; }
  html, body {
    width: 1200px; height: 1200px; overflow: hidden;
    background: var(--backdrop);
    font-family: "Montserrat", sans-serif;
  }
  .stage {
    width: 1200px; height: 1200px;
    display: flex; justify-content: center; align-items: center; gap: 60px;
  }
  .card {
    width: 420px; height: 720px; border-radius: 30px;
    position: relative; overflow: hidden;
  }

  /* Front */
  .card--front {
    background: var(--card-white);
    display: flex; flex-direction: column; align-items: center;
    padding-top: 110px; text-align: center; color: var(--ink);
  }
  .brand {
    display: flex; align-items: center; gap: 14px;
  }
  .brand__mark {
    width: 30px; height: 30px; background: var(--brand-yellow);
  }
  .brand__name {
    font-weight: 800; font-size: 50px; line-height: 1;
    color: var(--brand-yellow); letter-spacing: -0.5px;
  }
  .person { margin-top: 120px; }
  .person__name {
    font-weight: 700; font-size: 27px; color: var(--brand-yellow);
  }
  .person__role {
    font-size: 14px; color: var(--ink-soft); margin-top: 2px;
  }
  .contact-rule {
    display: flex; align-items: center; gap: 8px;
    width: 330px; margin-top: 18px;
  }
  .contact-rule__line { flex: 1; height: 2px; background: var(--brand-yellow); }
  .contact-rule__icon {
    width: 26px; height: 26px; border-radius: 4px;
    background: var(--brand-yellow);
    display: flex; align-items: center; justify-content: center;
  }
  .contact-list {
    list-style: none; margin-top: 18px;
    font-size: 16px; line-height: 1.45; color: var(--ink);
  }
  .divider {
    width: 90px; height: 2px; background: var(--brand-yellow); margin: 26px 0 22px;
  }
  .address { font-size: 15px; line-height: 1.45; color: var(--ink-soft); font-style: normal; }

  /* Back */
  .card--back { background: var(--card-dark); }
  .back__pattern {
    position: absolute; inset: 0 0 280px 0;
    background: linear-gradient(200deg, var(--pattern-light) 0%, var(--pattern-dark) 100%);
  }
  .back__brand {
    position: absolute; left: 0; right: 0; bottom: 90px;
    display: flex; justify-content: center;
  }
</style>
</head>
<body>
<main class="stage">
  <section class="card card--front" aria-label="Business card front">
    <div class="brand">
      <span class="brand__mark"></span>
      <span class="brand__name">Pixel Forum</span>
    </div>

    <div class="person">
      <h1 class="person__name">Dana Whitlow</h1>
      <p class="person__role">President</p>
    </div>

    <div class="contact-rule">
      <span class="contact-rule__line"></span>
      <span class="contact-rule__icon">
        <svg width="14" height="14" viewBox="0 0 24 24" aria-hidden="true"><path fill="#fff" d="M6.6 10.8a15 15 0 0 0 6.6 6.6l2.2-2.2c.3-.3.7-.4 1-.2 1.1.4 2.3.6 3.6.6.6 0 1 .4 1 1V20c0 .6-.4 1-1 1A17 17 0 0 1 3 4c0-.6.4-1 1-1h3.5c.6 0 1 .4 1 1 0 1.2.2 2.4.6 3.6.1.3 0 .7-.2 1z"/></svg>
      </span>
      <span class="contact-rule__icon">
        <svg width="14" height="14" viewBox="0 0 24 24" aria-hidden="true"><rect x="2" y="5" width="20" height="14" rx="2" fill="#fff"/><path d="M3 6l9 7 9-7" fill="none" stroke="#f6c400" stroke-width="2"/></svg>
      </span>
      <span class="contact-rule__icon">
        <svg width="14" height="14" viewBox="0 0 24 24" aria-hidden="true"><circle cx="12" cy="12" r="9" fill="none" stroke="#fff" stroke-width="2"/><path d="M3 12h18M12 3c3 3 3 15 0 18M12 3c-3 3-3 15 0 18" fill="none" stroke="#fff" stroke-width="1.6"/></svg>
      </span>
      <span class="contact-rule__line"></span>
    </div>

    <ul class="contact-list">
      <li>1-555-010-4477</li>
      <li>info@pixelforum-arch.com</li>
      <li>www.pixelforum-arch.com</li>
    </ul>

    <span class="divider"></span>

    <address class="address">48 Linden Court<br>Fairhaven NY 10000</address>
  </section>

  <section class="card card--back" aria-label="Business card back">
    <div class="back__pattern" role="img" aria-label="Repeating grey brand pattern fading from light to dark"></div>
    <div class="back__brand">
      <div class="brand">
        <span class="brand__mark"></span>
        <span class="brand__name">Pixel Forum</span>
      </div>
    </div>
  </section>
</main>
</body>
</html>
```